Pet Care Business Card

Dog & Cat Grooming, we come to you or come to Tails and Whiskers Nook
Doggy day care,
Boutique holiday care,
Pet Supplies
All Natural Products used
Have created the logo, which I will forward shortly but need help to have it on flyers business cards ect
email tailsandwhiskersnook@furmail.example
Ph: 0417552630
Colours: Green Black and paws prints nott sure what colour for them
Thank you to all that forwarded their designs, very hard choice and I thank you for your effort, shall recommend this to all my collegues
Thanks Again Jo :)
Business
0417552630
57 upper Kestrel Lane
Brindle QLD 4512

```html
<!DOCTYPE html>
<html lang="en">
<head>
<meta charset="utf-8">
<title>Tails and Whiskers Nook – Business Cards</title>
<link rel="stylesheet" href="https://fonts.googleapis.com/css2?family=Lato:wght@400;700&display=swap">
<style>
  :root {
    --backdrop: #ecebe8;
    --teal: #2ec6c1;
    --teal-deep: #16a9a6;
    --teal-light: #45d4cf;
    --ink: #1d2626;
    --paper: #ffffff;
    --muted: #2f5f5d;
  }
  * { box-sizing: border-box; margin: 0; padding: 0; }
  html, body {
    width: 1200px; height: 1023px; overflow: hidden;
    background: var(--backdrop);
    font-family: "Lato", sans-serif;
  }
  .canvas { position: relative; width: 1200px; height: 1023px; }

  .card {
    position: absolute;
    width: 560px; height: 320px;
    border-radius: 6px;
    background: linear-gradient(135deg, var(--teal-light) 0%, var(--teal) 50%, var(--teal-deep) 100%);
    box-shadow: 0 14px 30px rgba(0,0,0,.18);
    overflow: hidden;
  }
  .card--front { left: 90px; top: 110px; }
  .card--back  { left: 550px; top: 560px; }

  /* front */
  .pad-pattern {
    position: absolute; right: 0; top: 0; width: 330px; height: 190px;
    background: radial-gradient(ellipse at 70% 30%, rgba(0,0,0,.07), rgba(0,0,0,0) 70%);
  }
  .brand { position: absolute; left: 34px; top: 40px; display: flex; align-items: center; gap: 14px; }
  .brand__square { width: 54px; height: 54px; border: 4px solid var(--ink); border-radius: 4px; }
  .brand__name { color: var(--paper); font-weight: 400; font-size: 22px; letter-spacing: 1px; text-transform: uppercase; line-height: 1.1; }
  .brand__name span { display: block; font-size: 13px; letter-spacing: 8px; text-transform: lowercase; }

  .person { position: absolute; left: 34px; top: 150px; }
  .person__name { color: var(--muted); font-size: 24px; letter-spacing: 1px; text-transform: uppercase; }
  .person__role { color: var(--paper); font-size: 13px; margin-top: 2px; }

  .contact { position: absolute; left: 34px; top: 216px; list-style: none; }
  .contact li { display: flex; align-items: center; gap: 9px; color: var(--paper); font-size: 13px; margin-bottom: 7px; }
  .contact svg { width: 16px; height: 16px; flex: none; }

  /* back */
  .services { position: absolute; left: 34px; top: 36px; list-style: none; }
  .services li { display: flex; align-items: center; gap: 10px; color: var(--ink); font-size: 15px; margin-bottom: 8px; }
  .services li::before { content: ""; width: 9px; height: 9px; border-radius: 50%; background: var(--ink); }

  .back-brand { position: absolute; left: 34px; bottom: 40px; color: var(--paper); font-size: 24px; letter-spacing: 1px; text-transform: uppercase; line-height: 1.1; }
  .back-brand span { display: block; font-size: 14px; letter-spacing: 9px; text-transform: lowercase; }
  .back-square { position: absolute; right: 36px; bottom: 36px; width: 170px; height: 170px; border: 7px solid var(--ink); border-radius: 6px; }
</style>
</head>
<body>
<main class="canvas">

  <section class="card card--front" aria-label="Business card front">
    <div class="pad-pattern" role="img" aria-label="Faint paw print pattern"></div>
    <div class="brand">
      <div class="brand__square"></div>
      <p class="brand__name">Tails and Whiskers<span>nook</span></p>
    </div>
    <div class="person">
      <p class="person__name">Daniel Hurst</p>
      <p class="person__role">Director</p>
    </div>
    <ul class="contact">
      <li>
        <svg viewBox="0 0 16 16"><rect width="16" height="16" rx="3" fill="#1d2626"/><path d="M5 3.5l2 2-1 1.2c.6 1.4 1.7 2.5 3 3.1l1.2-1 2 2-1.3 1.7C7.5 12 4 8.5 3.5 5z" fill="#2ec6c1"/></svg>
        0417552630
      </li>
      <li>
        <svg viewBox="0 0 16 16"><rect width="16" height="16" rx="3" fill="#1d2626"/><rect x="3" y="4.5" width="10" height="7" fill="none" stroke="#2ec6c1" stroke-width="1.3"/><path d="M3 4.5l5 4 5-4" fill="none" stroke="#2ec6c1" stroke-width="1.3"/></svg>
        tailsandwhiskersnook@furmail.example
      </li>
      <li>
        <svg viewBox="0 0 16 16"><rect width="16" height="16" rx="3" fill="#1d2626"/><path d="M8 13s-3.5-4-3.5-6.5a3.5 3.5 0 017 0C11.5 9 8 13 8 13z" fill="#2ec6c1"/><circle cx="8" cy="6.5" r="1.2" fill="#1d2626"/></svg>
        57 upper Kestrel Lane Brindle QLD 4512
      </li>
    </ul>
  </section>

  <section class="card card--back" aria-label="Business card back">
    <ul class="services">
      <li>Dog &amp; Cat Grooming</li>
      <li>Doggy Day Care</li>
      <li>Boutique Holiday Care</li>
      <li>Pet Supplies</li>
      <li>All Natural Products Used</li>
    </ul>
    <p class="back-brand">Tails and Whiskers<span>nook</span></p>
    <div class="back-square"></div>
  </section>

</main>
</body>
</html>
```